Brightford Lingua Partners, LLC

We need a business card that includes information about our business and conveys a reliable business that provides document translation services and interpreters for a variety of corporate and individual clients. We want to come across as professional, reliable, yet approachable. It should include the following on one side:

ESL / ENL Language Classes, Private Lessons, and Online Tutors
PALQE Training and Testing
Translating & Interpreting Services
Contact us about Over-the-Phone Interpreting in over 200 languages
24/7/365
www.brightfordlingua.example

The other side should include (555) 481-3062

Marla Quennick, President
412 Garvin Ave., Ste. 209
Indianapolis, IN 46999
Updates

Please add USA as part of the address. Also, please add mrqquennick@brightfordlinguapartners.example as the e-mail address. Thank you.

Target Market(s)

Business professionals, their families, the international community

Industry/Entity Type

Business

Contact Information for Business Card

24/7/365
www.brightfordlingua.example

(555) 481-3062

Marla Quennick, President
412 Garvin Ave., Ste. 209
Indianapolis, IN 46999
USA

Font styles to use
Sans Serif

Colors

Designer to choose colors to be used in the design.

Requirements
Must have
• See project description
• e-mail address and web address
• Phone number
Nice to have
• a globe
• physical address
Should not have
• Should not have the same color scheme as other agencies in our market in Indiana unless it is blue and black. No purple or yellow.

```html
<!DOCTYPE html>
<html lang="en">
<head>
<meta charset="utf-8">
<title>Brightford Lingua Partners – Business Card</title>
<link href="https://fonts.googleapis.com/css2?family=Lato:wght@400;700&display=swap" rel="stylesheet">
<style>
  :root {
    --backdrop: #d3d4d6;
    --ink: #000000;
    --paper: #ffffff;
    --brand-blue: #2394d3;
    --brand-blue-dark: #17648f;
    --globe-tint: #161210;
  }
  html, body {
    margin: 0;
    padding: 0;
    width: 1200px;
    height: 1200px;
    overflow: hidden;
    background: var(--backdrop);
  }
  .canvas {
    position: relative;
    width: 1200px;
    height: 1200px;
  }
  .card {
    position: absolute;
    left: 264px;
    width: 694px;
    height: 397px;
    font-family: "Lato", sans-serif;
  }
  .card--front { top: 146px; }
  .card--back  { top: 656px; }
  .card svg { display: block; }
  .wordmark { font-family: "Lato", sans-serif; font-weight: 400; }
  .services-list { font-family: "Lato", sans-serif; font-size: 13px; fill: var(--paper); }
  .holder-name { font-family: "Lato", sans-serif; font-weight: 700; font-size: 30px; fill: var(--brand-blue); }
  .holder-role { font-family: "Lato", sans-serif; font-size: 21px; fill: var(--paper); }
  .contact-line { font-family: "Lato", sans-serif; font-size: 13px; fill: var(--paper); }
</style>
</head>
<body>
<main class="canvas">

  <!-- Front side -->
  <section class="card card--front" aria-label="Business card front">
    <svg width="694" height="397" viewBox="0 0 694 397">
      <rect class="card-paper" x="0" y="0" width="694" height="397" fill="var(--paper)"/>
      <rect class="card-field" x="46" y="0" width="598" height="397" fill="var(--ink)"/>

      <g class="globe-decoration" role="img" aria-label="Faint world globe in the background">
        <circle cx="342" cy="198" r="196" fill="var(--globe-tint)"/>
      </g>

      <g class="side-tab side-tab--left">
        <polygon points="34,89 46,80 46,89" fill="var(--brand-blue-dark)"/>
        <polygon points="34,323 46,323 46,332" fill="var(--brand-blue-dark)"/>
        <rect x="34" y="89" width="31" height="234" fill="var(--brand-blue)"/>
      </g>
      <g class="side-tab side-tab--right">
        <polygon points="656,89 644,80 644,89" fill="var(--brand-blue-dark)"/>
        <polygon points="656,323 644,323 644,332" fill="var(--brand-blue-dark)"/>
        <rect x="625" y="89" width="31" height="234" fill="var(--brand-blue)"/>
      </g>

      <g class="brand-lockup">
        <circle cx="254" cy="146" r="68" fill="var(--paper)"/>
        <text class="wordmark" fill="var(--paper)" font-size="38">
          <tspan x="332" y="122">Brightford</tspan>
          <tspan x="332" y="164">Lingua</tspan>
          <tspan x="332" y="206">Partners</tspan><tspan font-size="18" dx="6">LLC</tspan>
        </text>
      </g>

      <text class="services-list" text-anchor="middle">
        <tspan x="347" y="251">ESL / ENL Language Classes, Private Lessons, and Online Tutors</tspan>
        <tspan x="347" y="267">PALQE Training and Testing</tspan>
        <tspan x="347" y="284">Translating &amp; Interpreting Services</tspan>
        <tspan x="347" y="301">Contact us about Over-the-Phone Interpreting in over 200 languages</tspan>
        <tspan x="347" y="317">24/7/365</tspan>
      </text>
    </svg>
  </section>

  <!-- Back side -->
  <section class="card card--back" aria-label="Business card back">
    <svg width="694" height="397" viewBox="0 0 694 397">
      <rect class="card-field" x="0" y="0" width="694" height="397" fill="var(--ink)"/>
      <rect class="logo-panel" x="60" y="0" width="286" height="397" fill="var(--paper)"/>

      <g class="brand-lockup">
        <circle cx="128" cy="200" r="50" fill="var(--brand-blue)"/>
        <text class="wordmark" fill="var(--ink)" font-size="27">
          <tspan x="184" y="180">Brightford</tspan>
          <tspan x="184" y="212">Lingua</tspan>
          <tspan x="184" y="244">Partners</tspan><tspan font-size="13" dx="4">LLC</tspan>
        </text>
      </g>

      <g class="contact-tab">
        <polygon points="334,134 346,124 346,134" fill="var(--brand-blue-dark)"/>
        <polygon points="334,286 346,286 346,296" fill="var(--brand-blue-dark)"/>
        <rect x="334" y="134" width="32" height="152" fill="var(--brand-blue)"/>
      </g>

      <text class="holder-name" x="376" y="84">Marla Quennick</text>
      <text class="holder-role" x="379" y="108">President</text>

      <g class="contact-icons" fill="var(--ink)">
        <g class="icon icon--phone">
          <circle cx="351" cy="176" r="6.5"/>
          <path d="M348.2,172.6 l1.6,-0.4 l1,2.2 l-1,0.8 q0.8,1.8 2.4,2.6 l0.8,-1 l2.2,1 l-0.4,1.6 q-4.8,0.4 -6.6,-6.8z" fill="var(--paper)"/>
        </g>
        <g class="icon icon--email">
          <circle cx="351" cy="198" r="6.5"/>
          <text x="351" y="201.2" text-anchor="middle" font-size="9" font-weight="700" fill="var(--paper)" font-family="Lato, sans-serif">@</text>
        </g>
        <g class="icon icon--web">
          <circle cx="351" cy="220" r="6.5"/>
          <path d="M348.3,222.7 l5.4,-5.4" stroke="var(--paper)" stroke-width="1.2"/>
          <rect x="346.8" y="220.2" width="4" height="2.4" rx="1.2" transform="rotate(-45 348.8 221.4)" fill="none" stroke="var(--paper)" stroke-width="0.9"/>
          <rect x="351.2" y="217.4" width="4" height="2.4" rx="1.2" transform="rotate(-45 353.2 218.6)" fill="none" stroke="var(--paper)" stroke-width="0.9"/>
        </g>
        <g class="icon icon--pin">
          <circle cx="351" cy="244" r="6.5"/>
          <path d="M351,248.2 q-3,-3.4 -3,-5.4 a3,3 0 0 1 6,0 q0,2 -3,5.4z" fill="var(--paper)"/>
          <circle cx="351" cy="242.8" r="1" fill="var(--ink)"/>
        </g>
      </g>

      <text class="contact-line" x="379" y="180">(555) 481-3062</text>
      <text class="contact-line" x="379" y="202">mrqquennick@brightfordlinguapartners.example</text>
      <text class="contact-line" x="379" y="224">www.brightfordlingua.example</text>
      <text class="contact-line">
        <tspan x="379" y="248">412 Garvin Ave., Ste. 209</tspan>
        <tspan x="379" y="264">Indianapolis, IN 46999</tspan>
        <tspan x="379" y="280">USA</tspan>
      </text>
    </svg>
  </section>

</main>
</body>
</html>
```